Homemaker goats milk soap label

The name of my farm is Fern N Heron Farm. I would like to keep my label vintage 1800s is appearance. A linked to my webpage, still under development is http://lopo.mivtrel.com/dev2/pastureway/. This will give you a feel for my theme. Along with other goat and bison by products, I make and sell homemade goat milk soap and I would like a special label to package my fabulous soap.
Updates

Hello Designers, To assist you with designing my label, I have attached a new photo from Lather Harbor that shows the type label I am going to use.

Industry/Entity Type

Farm

```html
<!DOCTYPE html>
<html lang="en">
<head>
<meta charset="utf-8">
<title>Fern N Heron Goats Milk Soap Labels</title>
<link rel="stylesheet" href="https://fonts.googleapis.com/css2?family=Pathway+Gothic+One&family=Alfa+Slab+One&family=Open+Sans:ital@0;1&display=swap">
<style>
  :root {
    --page: #ffffff;
    --label-cream: #faf6b6;
    --label-tan: #dccb98;
    --stripe-tan: rgba(200, 178, 120, 0.35);
    --stripe-lime: rgba(214, 228, 170, 0.7);
    --stripe-lavender: rgba(220, 190, 222, 0.85);
    --ink-brown: #8b7457;
    --ink-brown-soft: #a48d6c;
    --art-light: #efe3b0;
    --art-mid: #c9b284;
    --art-dark: #9c8461;
    --vanilla: #8b7457;
    --lime: #e4edbe;
    --lavender: #dcc4e0;
    --template-line: #b9b9b9;
    --template-text: #6b6b6b;
    --glue-text: #b3b3b3;
  }
  html, body {
    margin: 0;
    padding: 0;
    width: 1200px;
    height: 1001px;
    overflow: hidden;
    background: var(--page);
  }
  .canvas {
    position: relative;
    width: 1200px;
    height: 1001px;
  }
  .label {
    position: absolute;
    top: 193px;
    width: 334px;
    height: 422px;
    overflow: hidden;
    --stripe: var(--stripe-tan);
    background:
      linear-gradient(180deg, rgba(250,246,182,0) 0%, rgba(250,246,182,0) 55%, rgba(205,185,130,0.55) 100%),
      repeating-linear-gradient(90deg, var(--label-cream) 0 22px, var(--stripe) 22px 40px),
      var(--label-cream);
  }
  .label--vanilla { left: 53px; }
  .label--lime { left: 437px; --stripe: var(--stripe-lime); }
  .label--lavender { left: 820px; --stripe: var(--stripe-lavender); }

  .label__tagline {
    position: absolute;
    left: 40px;
    top: 16px;
    margin: 0;
    font-family: "Pathway Gothic One", sans-serif;
    font-size: 38px;
    font-weight: 400;
    color: var(--ink-brown-soft);
    line-height: 1;
    white-space: nowrap;
  }
  .label__brand {
    position: absolute;
    left: 37px;
    top: 74px;
    margin: 0;
    font-family: "Alfa Slab One", serif;
    font-size: 31px;
    font-weight: 400;
    color: var(--ink-brown);
    line-height: 1;
    white-space: nowrap;
  }
  .label__product {
    position: absolute;
    left: 108px;
    top: 124px;
    margin: 0;
    font-family: "Pathway Gothic One", sans-serif;
    font-size: 41px;
    color: var(--ink-brown-soft);
    line-height: 1;
    white-space: nowrap;
  }
  .label__art {
    position: absolute;
    left: 12px;
    top: 204px;
    width: 306px;
    height: 192px;
  }
  .label__scent {
    position: absolute;
    top: 135px;
    left: 15px;
    width: 84px;
    height: 84px;
    border-radius: 50%;
    display: flex;
    align-items: center;
    justify-content: center;
    font-family: "Alfa Slab One", serif;
    font-size: 15px;
    color: var(--ink-brown);
  }
  .label--vanilla .label__scent { background: var(--vanilla); color: var(--label-cream); transform: rotate(-25deg); font-size: 17px; }
  .label--lime .label__scent { background: var(--lime); left: 21px; }
  .label--lavender .label__scent { background: var(--lavender); left: 23px; top: 140px; font-size: 12px; }

  .template {
    position: absolute;
    left: 0;
    top: 0;
    width: 1200px;
    height: 1001px;
  }
  .template__caption {
    position: absolute;
    left: 184px;
    top: 798px;
    margin: 0;
    font-family: "Open Sans", sans-serif;
    font-style: italic;
    font-size: 33px;
    color: var(--template-text);
  }
</style>
</head>
<body>
<main class="canvas">
  <svg width="0" height="0" style="position:absolute" aria-hidden="true">
    <defs>
      <radialGradient id="art-tone" cx="50%" cy="50%" r="55%">
        <stop offset="0%" stop-color="var(--art-mid)"/>
        <stop offset="60%" stop-color="var(--art-light)"/>
        <stop offset="100%" stop-color="var(--art-mid)"/>
      </radialGradient>
    </defs>
  </svg>

  <section class="label label--vanilla">
    <p class="label__tagline">Home Crafted</p>
    <h2 class="label__brand">Fern N Heron</h2>
    <p class="label__product">Goats Milk Soap</p>
    <svg class="label__art" viewBox="0 0 306 192" role="img" aria-label="Oval vignette with an engraved goat and bison illustration">
      <ellipse cx="153" cy="96" rx="149" ry="92" fill="url(#art-tone)" stroke="var(--art-dark)" stroke-width="6"/>
    </svg>
    <span class="label__scent">Vanilla</span>
  </section>

  <section class="label label--lime">
    <p class="label__tagline">Home Crafted</p>
    <h2 class="label__brand">Fern N Heron</h2>
    <p class="label__product">Goats Milk Soap</p>
    <svg class="label__art" viewBox="0 0 306 192" role="img" aria-label="Oval vignette with an engraved goat and bison illustration">
      <ellipse cx="153" cy="96" rx="149" ry="92" fill="url(#art-tone)" stroke="var(--art-dark)" stroke-width="6"/>
    </svg>
    <span class="label__scent">Lime</span>
  </section>

  <section class="label label--lavender">
    <p class="label__tagline">Home Crafted</p>
    <h2 class="label__brand">Fern N Heron</h2>
    <p class="label__product">Goats Milk Soap</p>
    <svg class="label__art" viewBox="0 0 306 192" role="img" aria-label="Oval vignette with an engraved goat and bison illustration">
      <ellipse cx="153" cy="96" rx="149" ry="92" fill="url(#art-tone)" stroke="var(--art-dark)" stroke-width="6"/>
    </svg>
    <span class="label__scent">Lavender</span>
  </section>

  <p class="template__caption">Template</p>
  <svg class="template" viewBox="0 0 1200 1001" aria-label="Label folding template">
    <g fill="none" stroke="var(--template-line)" stroke-width="2">
      <rect x="359" y="668" width="658" height="300"/>
      <line x1="459" y1="668" x2="459" y2="968"/>
      <line x1="688" y1="668" x2="688" y2="968"/>
      <line x1="789" y1="668" x2="789" y2="968"/>
      <line x1="982" y1="672" x2="982" y2="964" stroke-dasharray="2 6"/>
    </g>
    <g font-family="Open Sans, sans-serif" font-size="33" fill="var(--template-text)">
      <text transform="translate(409 818) rotate(-90)" text-anchor="middle" dominant-baseline="middle">Side</text>
      <text x="573" y="832" text-anchor="middle">Front</text>
      <text transform="translate(742 818) rotate(-90)" text-anchor="middle" dominant-baseline="middle">Side</text>
      <text x="902" y="832" text-anchor="middle">Back</text>
      <text transform="translate(1001 816) rotate(-90)" text-anchor="middle" dominant-baseline="middle" fill="var(--glue-text)">Glue</text>
    </g>
  </svg>

</main>
</body>
</html>
```